Web design for software company

I'm a software developer that designs high end specialist web applications, mobile apps and user friendly applications for medium to large customers. I integrate different systems together within a company and provide web based applications or mobile apps to view and edit information in that web of linked systems.

I currently work alone, basically selling my time on specialist projects, but also build my own software solutions which I eventually want to put into the market.

My company name is Overthread (lowercase 'L' for logic) and I work from the Netherlands. I've attached my current logo which is basically just text in VOXbox font. Current colours are mustard yellow and grey, but i'm open to other options to better fit the web design.

I've got a sort of slogan: "Specialized software development" - better ideas are welcome. The slogan in the logo attachment is older.

I'm looking for a site design that reflects my work as being on the cutting edge of technology, but being clear and simple. My thinking with the name Overthread is that it refers to the underlying mechanism and logic of software.

The site will not be text heavy, so some kind of large graphic to do with software design is welcome. I expect about 4 or 5 main pages or sections of the site in which i'll eventually add things like a blog or contact info etc.

Industry/Entity Type

It Company

Number of Pages Required

1 page

Font styles to use
Sans Serif

Requirements
Nice to have
• A large graphic or photo relevant to my focus as a software developer. Something that shows connecting of software systems with perhaps a variety of devices/browsers that would display data from that cloud of systems.
• Something like these (allthough these are ugly - but the idea is what i mean):
• http://img4.pixvaultimages.example/2000517/22458/i/450/pixvault_224581133-Cloud-computing-user-interface.jpg
• http://business.tamblinet.example/images/modules/mobile-device-policy-design-banner.png
• https://www.pagecraftly.example/images/responsive-web-design.jpg
• http://www.norvexa.example/images/web_apps.png
• https://www.keyportal.example/assets/img/product/web-app@2x.png?v2
Should not have
• Photographs of smiling happy people looking at a screen that make it look like it's a huge business with many offices. I'm a one-man company which could perhaps grow a little bit, but i want to focus on my expertise instead of size.

```html
<!DOCTYPE html>
<html lang="en">
<head>
<meta charset="utf-8">
<title>Overthread — Pricing &amp; Blog</title>
<link href="https://fonts.googleapis.com/css2?family=Open+Sans:ital,wght@0,400;0,600;1,600&family=Source+Sans+Pro:wght@600;700&display=swap" rel="stylesheet">
<style>
  :root {
    --mustard: #c79100;
    --grey: #9a9a9a;
    --panel: #f4f4f7;
    --ink: #5f5f5f;
    --muted: #8a8a8a;
    --rule: #d8d8d8;
    --white: #ffffff;
  }
  * { box-sizing: border-box; margin: 0; padding: 0; }
  html, body { width: 1093px; height: 1200px; overflow: hidden; background: var(--white); }
  body { position: relative; font-family: "Open Sans", Arial, sans-serif; color: var(--ink); }

  .section-head { position: absolute; left: 0; width: 1093px; text-align: center; }
  .section-title { font-family: "Source Sans Pro", Arial, sans-serif; font-weight: 700; font-size: 20px; letter-spacing: 2px; color: var(--ink); line-height: 1; }
  .section-lead { font-size: 8px; color: var(--muted); margin-top: 13px; line-height: 1; }
  .divider { position: relative; width: 112px; height: 6px; margin: 17px auto 0; }
  .divider::before, .divider::after { content: ""; position: absolute; top: 2px; width: 46px; height: 1px; background: #bdbdbd; }
  .divider::before { left: 0; }
  .divider::after { right: 0; }
  .divider span { position: absolute; left: 53px; top: 0; width: 5px; height: 5px; border-radius: 50%; background: var(--mustard); }

  .pricing-head { top: 86px; }
  .plans { position: absolute; top: 186px; left: 211px; display: flex; gap: 10px; }
  .plan { position: relative; width: 217px; height: 346px; background: var(--panel); text-align: center; }
  .plan-top { height: 117px; background: var(--grey); padding-top: 24px; }
  .plan--featured .plan-top { background: var(--mustard); }
  .plan-name { font-family: "Source Sans Pro", Arial, sans-serif; font-weight: 700; font-size: 15px; letter-spacing: 1.5px; color: var(--white); line-height: 1; }
  .price-ring { position: absolute; left: 58px; top: 67px; width: 100px; height: 100px; border-radius: 50%; background: rgba(255,255,255,0.35); }
  .price-disc { position: absolute; left: 6px; top: 6px; width: 88px; height: 88px; border-radius: 50%; background: var(--white); padding-top: 26px; }
  .price { font-family: "Source Sans Pro", Arial, sans-serif; font-weight: 700; font-size: 22px; color: var(--grey); line-height: 1; }
  .plan--featured .price { color: var(--mustard); }
  .per { font-size: 7px; color: var(--muted); margin-top: 3px; }
  .features { list-style: none; position: absolute; top: 184px; left: 0; width: 100%; }
  .features li { font-size: 8px; color: var(--muted); line-height: 23px; }
  .choose { position: absolute; left: 67px; top: 292px; width: 83px; height: 26px; border: 0; background: var(--grey); color: var(--white); font-family: "Open Sans", Arial, sans-serif; font-size: 7px; box-shadow: 0 2px 3px rgba(0,0,0,0.25); }
  .plan--featured .choose { background: var(--mustard); }

  .split { position: absolute; top: 598px; left: 0; width: 1093px; height: 1px; background: var(--rule); }
  .blog-head { top: 664px; }

  .posts { position: absolute; top: 764px; left: 0; width: 1093px; }
  .tile { position: absolute; height: 274px; }
  .photo { overflow: hidden; }
  .post { background: var(--mustard); color: var(--white); padding: 44px 28px 0; z-index: 2; }
  .post::before { content: ""; position: absolute; top: 123px; border-top: 14px solid transparent; border-bottom: 14px solid transparent; }
  .post--left::before { left: -14px; border-right: 14px solid var(--mustard); }
  .post--right::before { right: -14px; border-left: 14px solid var(--mustard); }
  .client { font-size: 7.5px; line-height: 1; }
  .post-title { font-family: "Source Sans Pro", Arial, sans-serif; font-weight: 600; font-size: 13px; letter-spacing: 1.3px; margin-top: 17px; line-height: 1; }
  .post-title::after { content: ""; display: block; width: 25px; height: 2px; background: var(--white); margin-top: 9px; }
  .excerpt { font-size: 9.5px; line-height: 17px; margin-top: 22px; max-width: 222px; }
  .read-more { display: inline-block; margin-top: 23px; font-style: italic; font-weight: 600; font-size: 10px; color: var(--white); text-decoration: none; }
  .read-more svg { vertical-align: middle; margin-left: 4px; }
</style>
</head>
<body>

<header class="section-head pricing-head">
  <h2 class="section-title">OUR PRICING</h2>
  <p class="section-lead">A 30 days free trial for all. A brief story about how this process works, keep an eye till the end.</p>
  <div class="divider"><span></span></div>
</header>

<section class="plans">
  <article class="plan">
    <div class="plan-top"><h3 class="plan-name">STARTER</h3></div>
    <div class="price-ring"><div class="price-disc"><div class="price">$19</div><div class="per">per month</div></div></div>
    <ul class="features"><li>Competition Analysis Methods</li><li>All Ranked URLs</li><li>International Support System</li><li>Social Media Tracking</li></ul>
    <button class="choose">CHOOSE PLAN</button>
  </article>
  <article class="plan plan--featured">
    <div class="plan-top"><h3 class="plan-name">PREMIUM</h3></div>
    <div class="price-ring"><div class="price-disc"><div class="price">$39</div><div class="per">per month</div></div></div>
    <ul class="features"><li>Competition Analysis Methods</li><li>All Ranked URLs</li><li>International Support System</li><li>Social Media Tracking</li></ul>
    <button class="choose">CHOOSE PLAN</button>
  </article>
  <article class="plan">
    <div class="plan-top"><h3 class="plan-name">BUSINESS</h3></div>
    <div class="price-ring"><div class="price-disc"><div class="price">$99</div><div class="per">per month</div></div></div>
    <ul class="features"><li>Competition Analysis Methods</li><li>All Ranked URLs</li><li>International Support System</li><li>Social Media Tracking</li></ul>
    <button class="choose">CHOOSE PLAN</button>
  </article>
</section>

<div class="split"></div>

<header class="section-head blog-head">
  <h2 class="section-title" style="letter-spacing:0.5px">OUR BLOG</h2>
  <p class="section-lead">Suspendisse sed eros mollis, tincidunt felis eget, interdum eratullam sit amet odio.</p>
  <div class="divider"><span></span></div>
</header>

<section class="posts">
  <div class="tile photo" style="left:0;top:0;width:271px;background:linear-gradient(160deg,#4a3a30 0%,#6e4027 55%,#3c2416 100%)" role="img" aria-label="Photo of a latte on a wooden counter beside a brass bell and receipts"></div>
  <article class="tile post post--left" style="left:271px;top:0;width:274px">
    <p class="client">Tea Co.</p>
    <h3 class="post-title">APPS DESIGN</h3>
    <p class="excerpt">Lorem Ipsum is simply dummy text of the printing and typesetting industry. Lorem Ipsum has been the indu Stry's standard dummy text ever since the 1500s, an unknown printer took a galley of type a scrambled it to make a type specimen book.</p>
    <a class="read-more" href="#">Read More<svg width="7" height="7" viewBox="0 0 7 7"><path d="M1 1l2.5 2.5L1 6M3.5 1L6 3.5 3.5 6" fill="none" stroke="#fff" stroke-width="1.2"/></svg></a>
  </article>
  <div class="tile photo" style="left:545px;top:0;width:273px;background:radial-gradient(circle at 45% 50%,#f1efe6 0%,#e2e0d6 45%,#c8d3de 75%,#b9a578 100%)" role="img" aria-label="Close-up photo of an alarm clock face"></div>
  <article class="tile post post--left" style="left:818px;top:0;width:275px">
    <p class="client">Watch Co.</p>
    <h3 class="post-title">APPS IMPLEMENT</h3>
    <p class="excerpt">Lorem Ipsum is simply dummy text of the printing and typesetting industry. Lorem Ipsum has been the indu Stry's standard dummy text ever since the 1500s, an unknown printer took a galley of type a scrambled it to make a type specimen book.</p>
    <a class="read-more" href="#">Read More<svg width="7" height="7" viewBox="0 0 7 7"><path d="M1 1l2.5 2.5L1 6M3.5 1L6 3.5 3.5 6" fill="none" stroke="#fff" stroke-width="1.2"/></svg></a>
  </article>

  <article class="tile post post--right" style="left:0;top:274px;width:271px">
    <p class="client">Construction Co.</p>
    <h3 class="post-title">ERP DESIGN</h3>
    <p class="excerpt">Lorem Ipsum is simply dummy text of the printing and typesetting industry. Lorem Ipsum has been the indu Stry's standard dummy text ever since the 1500s, an unknown printer took a galley of type a scrambled it to make a type specimen book.</p>
  </article>
  <div class="tile photo" style="left:271px;top:274px;width:274px;background:linear-gradient(180deg,#c9d2d8 0%,#9aa4a8 40%,#3b3b3a 65%,#6a6249 100%)" role="img" aria-label="Photo of a road leading toward dark mountains"></div>
  <article class="tile post post--right" style="left:545px;top:274px;width:273px">
    <p class="client">Transport Co.</p>
    <h3 class="post-title">MAP FINDER APP</h3>
    <p class="excerpt">Lorem Ipsum is simply dummy text of the printing and typesetting industry. Lorem Ipsum has been the indu Stry's standard dummy text ever since the 1500s, an unknown printer took a galley of type a scrambled it to make a type specimen book.</p>
  </article>
  <div class="tile photo" style="left:818px;top:274px;width:275px;background:linear-gradient(180deg,#3d4a3a 0%,#5b6a4c 45%,#a8b07a 75%,#8f9868 100%)" role="img" aria-label="Photo of a vintage green car among trees"></div>
</section>

</body>
</html>
```